velmorino.eu :: Design ideas (no coding) for key pages of Personalized greeting cards online store

We need your vision on modern, clean, easy to read user interface (UI) for online service of personalized printed products, like greeting cards, postcards, fridge magnets, clips and etc.
Your vision should include UI presentation for:
- Home page with login (including soc nets)
- Product Designer page
- Cart pages (products and address selection)
- Example of general internal page (pricing, terms, etc)
- Artist info and portfolio page
We are looking for ideas we will love, NOT complete design of a whole site.
Top design/vision will we used as a basement for separate contract on complete design of the site.

UI should be based on existing functionality with some extent. It should not break ideas or methods used on prototype but designers are free to offer own product presentations, designer’s layout and cart views.

Prototype:
English: http://velmorino.eu
Russian: http://velmorino.ru
Lithuanian: http://velmorino.lt

Target Market(s)

People of 16-45 y.o. who likes to be distinctive, personal.

Industry/Entity Type

Store

Requirements
Must have
• Your work should meet attached requirements.
Site is multilingual. Wording should assume varieties in length on different languages.
Clean and easy to read UI
Flat design preferrably
Should be based on assets which are free or available for royalty-free licensing
Should not have
• heavy, meaningless 3D and shadow effects
Show NOT copy sites like: plonkra.com, tarnwick.co.uk

```html
<!DOCTYPE html>
<html lang="en">
<head>
<meta charset="utf-8">
<title>velmorino — greeting cards</title>
<link href="https://fonts.googleapis.com/css2?family=Roboto:ital,wght@0,400;0,500;0,700;1,700&display=swap" rel="stylesheet">
<style>
:root{
  --bg:#f5dcc5;
  --pink:#e07873;
  --pink-dark:#c9605b;
  --teal:#24948f;
  --orange:#f08a53;
  --navy:#2f5b82;
  --navy-dark:#244a6c;
  --brown:#984c40;
  --sand:#e7c7aa;
  --white:#fff;
  --ink:#5a4a40;
  --price:#e58a86;
  --btn:#f5b06a;
}
*{box-sizing:border-box;margin:0;padding:0}
html,body{width:771px;height:1200px;overflow:hidden}
body{background:var(--bg);font-family:"Roboto",sans-serif;position:relative;color:var(--ink)}
.abs{position:absolute}
.brand{left:86px;top:30px;display:flex;align-items:center;gap:8px}
.brand-dot{width:26px;height:26px;background:var(--pink-dark);border-radius:4px}
.brand-name{font-size:22px;font-weight:500;color:var(--brown)}
.cat-tab{top:48px;width:83px;height:52px;background:var(--pink);border-radius:5px;box-shadow:0 2px 0 var(--pink-dark)}
.cat-tab::after{content:"";position:absolute;left:37px;bottom:-5px;border:5px solid transparent;border-top-color:var(--pink);border-bottom:0}
.card-shape{position:absolute;background:var(--white);border-radius:4px}
.top-btn{top:48px;height:24px;border-radius:6px;color:#fff;font-size:10px;font-weight:500;display:flex;align-items:center;justify-content:center;gap:5px}
.login-btn{left:542px;width:68px;background:var(--navy)}
.contacts-btn{left:613px;width:68px;background:var(--orange)}
.nav{left:83px;top:106px;width:441px;height:44px;background:var(--white);border-radius:4px;box-shadow:0 2px 0 #e3c4a8}
.nav-all{position:absolute;left:0;top:0;width:122px;height:44px;background:var(--pink);border-radius:4px 0 0 4px;color:#fff;font-size:9px;font-weight:500;display:flex;align-items:center;justify-content:center}
.nav-item{position:absolute;top:18px;font-size:9px;color:#6b5e55}
.chev{position:absolute;top:30px;width:8px;height:6px}
.search{left:83px;top:156px;width:599px;height:43px;background:#fff;border-radius:6px;padding:6px}
.search-field{width:100%;height:100%;background:#f5f5f5;border:1px solid #ddd;border-radius:5px}
.swatches{left:83px;top:207px;width:599px;height:31px;display:flex;border-radius:4px;overflow:hidden}
.swatches span{flex:1}
.drop{width:114px;border-radius:4px;overflow:hidden;box-shadow:0 3px 0 rgba(0,0,0,.12)}
.drop div{height:34px;background:var(--pink);color:#fff;font-size:9px;font-weight:500;display:flex;align-items:center;justify-content:center;border-bottom:1px solid var(--pink-dark)}
.drop div.head{background:var(--orange)}
.login-panel{left:525px;top:80px;width:147px;height:168px;background:var(--navy);border-radius:3px;padding:12px 13px}
.login-panel::before{content:"";position:absolute;left:67px;top:-6px;border:6px solid transparent;border-bottom-color:var(--navy);border-top:0}
.lp-field{height:30px;margin-bottom:3px;border-radius:4px;color:#fff;font-size:8px;font-weight:500;display:flex;align-items:center;justify-content:center}
.lp-input{background:var(--navy-dark)}
.lp-submit{background:var(--pink);height:28px}
.lp-signup{background:var(--teal);height:28px}
.lp-remember{display:flex;align-items:center;gap:8px;color:#c8d6e4;font-size:8px;margin-top:4px}
.lp-check{width:16px;height:16px;background:#fff;border-radius:3px;display:flex;align-items:center;justify-content:center}
.themes{left:83px;top:249px;width:141px;box-shadow:0 2px 0 #c9b5a1;border-radius:3px;overflow:hidden}
.themes div{height:28px;display:flex;align-items:center;justify-content:center;font-size:9.5px;font-weight:500;color:var(--teal);border-bottom:1px solid #e6d2bf}
.themes .t-head{background:var(--teal);color:#fff;font-size:11px;height:26px}
.themes .t-all{background:var(--orange);color:#fff}
.banner{left:237px;top:248px;width:445px;height:53px;background:var(--orange);border-radius:4px;color:#fff;font-size:36px;font-style:italic;font-weight:700;display:flex;align-items:center;justify-content:center;letter-spacing:1px}
.product{width:142px;height:227px;background:#fff;border-radius:4px;box-shadow:0 2px 0 #dcc2aa;overflow:hidden}
.product-photo{width:142px;height:160px;background:linear-gradient(180deg,#3f6b3a 0%,#8a9a82 35%,#d9d9cc 60%,#6a5a5a 85%,#3d3a5a 100%)}
.product-meta{padding:5px 5px 0;font-size:8.5px;font-weight:500;color:var(--teal);line-height:13px}
.product-meta .sep{color:#999;margin:0 3px}
.product-actions{display:flex;align-items:center;gap:6px;padding:4px 5px 0}
.p-btn{width:24px;height:24px;background:var(--btn);border-radius:3px;display:flex;align-items:center;justify-content:center;box-shadow:0 2px 0 #d88e4a}
.p-price{margin-left:auto;font-size:19px;color:var(--price)}
.pager{left:236px;top:1032px;width:295px;height:33px;background:var(--sand);border-radius:5px;box-shadow:0 2px 0 #c4a587;display:flex;align-items:center;font-size:8px;color:#fff;font-weight:500}
.pg{width:38px;text-align:center}
.pg-cur{width:22px;height:22px;background:var(--btn);border-radius:3px;display:flex;align-items:center;justify-content:center;margin:0 8px}
.pg-goto{margin-left:auto;margin-right:6px;width:33px;height:22px;background:var(--btn);border-radius:3px;display:flex;align-items:center;justify-content:center}
.pager-links{left:562px;top:1044px;font-size:8px;font-weight:700;color:#6b5e55;display:flex;gap:13px}
.social{left:128px;width:51px;height:51px;border-radius:4px;color:#fff;font-size:8px;font-weight:700;display:flex;align-items:center;justify-content:center;text-align:center}
.follow{left:122px;width:62px;height:18px;border-radius:4px;color:#fff;font-size:8px;display:flex;align-items:center;justify-content:center}
.fw{background:#4a6fc0}.cl{background:#4ab4e2}.cn{background:#e8604e}
.footer{left:0;top:1083px;width:771px;height:117px;background:var(--brown)}
.f-links{left:237px;top:1108px;color:#fff;font-size:11px;font-weight:700;line-height:15px}
.f-copy{left:85px;top:1166px;color:#fff;font-size:11px;font-weight:500}
.news{left:471px;top:1099px;width:211px;height:79px;background:var(--sand);border-radius:5px;padding:10px 15px}
.news h3{font-size:9.5px;font-weight:500;color:var(--brown)}
.news-field{margin-top:6px;height:22px;background:#fbe3cc;border:1px solid #b9927a;border-radius:3px;display:flex;align-items:center;font-size:8px;color:var(--brown)}
.news-icon{width:24px;height:100%;border-right:1px solid #b9927a;display:flex;align-items:center;justify-content:center}
.news-field span{padding-left:7px}
.news-btn{position:absolute;right:17px;bottom:6px;width:56px;height:16px;background:var(--teal);color:#fff;font-size:7px;display:flex;align-items:center;justify-content:center;border-radius:2px}
</style>
</head>
<body>

<div class="abs brand"><span class="brand-dot"></span><span class="brand-name">velmorino</span></div>

<div class="abs cat-tab" style="left:232px"><span class="card-shape" style="left:6px;top:6px;width:20px;height:38px"></span><span class="card-shape" style="left:28px;top:15px;width:44px;height:28px"></span></div>
<div class="abs cat-tab" style="left:330px"><span class="card-shape" style="left:26px;top:14px;width:30px;height:30px"></span></div>
<div class="abs cat-tab" style="left:428px"><span class="card-shape" style="left:6px;top:6px;width:30px;height:38px"></span><span class="card-shape" style="left:38px;top:15px;width:38px;height:28px"></span></div>

<div class="abs top-btn login-btn">Log In <svg width="9" height="7" viewBox="0 0 9 7"><path d="M1 1l3.5 4L8 1" stroke="#fff" stroke-width="2" fill="none"/></svg></div>
<div class="abs top-btn contacts-btn">Contacts <svg width="9" height="7" viewBox="0 0 9 7"><path d="M1 1l3.5 4L8 1" stroke="#fff" stroke-width="2" fill="none"/></svg></div>

<nav class="abs nav">
  <div class="nav-all">All medias</div>
  <span class="nav-item" style="left:160px">Greetings card</span>
  <svg class="chev" style="left:186px" viewBox="0 0 8 6"><path d="M1 1l3 3 3-3" stroke="#e07873" stroke-width="2" fill="none"/></svg>
  <span class="nav-item" style="left:262px">Square cards</span>
  <span class="nav-item" style="left:366px">Postcards</span>
  <svg class="chev" style="left:383px" viewBox="0 0 8 6"><path d="M1 1l3 3 3-3" stroke="#e07873" stroke-width="2" fill="none"/></svg>
</nav>

<div class="abs search"><div class="search-field"></div></div>

<div class="abs swatches">
  <span style="background:#6fa9a6"></span><span style="background:#f4e9d6"></span><span style="background:#e3e3e3"></span><span style="background:#cacaca"></span><span style="background:#f6cccf"></span><span style="background:#f2d1c4"></span><span style="background:#e7d6c6"></span><span style="background:#d4c2b2"></span><span style="background:#a8a8ad"></span><span style="background:#9cb27d"></span><span style="background:#e79d9c"></span><span style="background:#ebb6a8"></span><span style="background:#d9c7a4"></span><span style="background:#c8d4a9"></span><span style="background:#b8d08b"></span>
</div>

<aside class="abs themes">
  <div class="t-head">Themes</div>
  <div class="t-all">All</div>
  <div style="background:#fbeee2">Bears</div>
  <div style="background:#dcefe9">Birthday</div>
  <div style="background:#e3e3df">Cards</div>
  <div style="background:#fbe1dc">Cats</div>
  <div style="background:#d9e4dd">Congratulations!</div>
  <div style="background:#f7e0d8">Dog</div>
  <div style="background:#f6f1d6">Flowers</div>
  <div style="background:#e2f2dc">For children</div>
  <div style="background:#dcf3ee">Frindship</div>
  <div style="background:#f5d8ee">Love</div>
  <div style="background:#e6d8f1">Newborn</div>
  <div style="background:#f8dce0">Photos</div>
  <div style="background:#f6e8d8">Religion</div>
  <div style="background:#fae0e1">Valentine's</div>
</aside>

<div class="abs banner">Say it all with a card!!!</div>

<div class="abs drop" style="left:216px;top:151px">
  <div class="head">All medias</div><div>Standard cards</div><div>Mini cards</div><div>Nano cards</div>
</div>
<div class="abs drop" style="left:414px;top:151px">
  <div class="head">All medias</div><div>Postcard A4</div><div>Postcards XXL</div><div>Postcard XL</div><div>Standard postcard</div>
</div>

<div class="abs login-panel">
  <div class="lp-field lp-input">Username</div>
  <div class="lp-field lp-input">Password</div>
  <div class="lp-field lp-submit">SUBMIT</div>
  <div class="lp-field lp-signup">SIGN UP</div>
  <div class="lp-remember"><span class="lp-check"><svg width="11" height="9" viewBox="0 0 11 9"><path d="M1 4l3 3 6-6" stroke="#e07873" stroke-width="2" fill="none"/></svg></span>Remember</div>
</div>

<!-- product grid -->
<div class="abs product" style="left:237px;top:311px"><div class="product-photo" role="img" aria-label="Photo of a handmade New Year card"></div><div class="product-meta">Lina Corvath<span class="sep">|</span>Runa<br>Naujieji metai</div><div class="product-actions"><span class="p-btn"><svg width="13" height="12" viewBox="0 0 13 12"><path d="M6.5 11L1.5 6A3 3 0 016.5 2a3 3 0 015 4z" fill="#d787a8"/></svg></span><span class="p-btn"><svg width="14" height="12" viewBox="0 0 14 12"><path d="M1 1h2l2 7h7l1-5H4" stroke="#d787a8" stroke-width="1.5" fill="none"/><circle cx="6" cy="10.5" r="1" fill="#d787a8"/><circle cx="11" cy="10.5" r="1" fill="#d787a8"/></svg></span><span class="p-price">€0.00</span></div></div>
<div class="abs product" style="left:390px;top:311px"><div class="product-photo" role="img" aria-label="Photo of a handmade New Year card"></div><div class="product-meta">Lina Corvath<span class="sep">|</span>Runa<br>Naujieji metai</div><div class="product-actions"><span class="p-btn"><svg width="13" height="12" viewBox="0 0 13 12"><path d="M6.5 11L1.5 6A3 3 0 016.5 2a3 3 0 015 4z" fill="#d787a8"/></svg></span><span class="p-btn"><svg width="14" height="12" viewBox="0 0 14 12"><path d="M1 1h2l2 7h7l1-5H4" stroke="#d787a8" stroke-width="1.5" fill="none"/><circle cx="6" cy="10.5" r="1" fill="#d787a8"/><circle cx="11" cy="10.5" r="1" fill="#d787a8"/></svg></span><span class="p-price">€0.00</span></div></div>
<div class="abs product" style="left:542px;top:311px"><div class="product-photo" role="img" aria-label="Photo of a handmade New Year card"></div><div class="product-meta">Lina Corvath<span class="sep">|</span>Runa<br>Naujieji metai</div><div class="product-actions"><span class="p-btn"><svg width="13" height="12" viewBox="0 0 13 12"><path d="M6.5 11L1.5 6A3 3 0 016.5 2a3 3 0 015 4z" fill="#d787a8"/></svg></span><span class="p-btn"><svg width="14" height="12" viewBox="0 0 14 12"><path d="M1 1h2l2 7h7l1-5H4" stroke="#d787a8" stroke-width="1.5" fill="none"/><circle cx="6" cy="10.5" r="1" fill="#d787a8"/><circle cx="11" cy="10.5" r="1" fill="#d787a8"/></svg></span><span class="p-price">€0.00</span></div></div>

<div class="abs product" style="left:237px;top:549px"><div class="product-photo" role="img" aria-label="Photo of a handmade New Year card"></div><div class="product-meta">Lina Corvath<span class="sep">|</span>Runa<br>Naujieji metai</div><div class="product-actions"><span class="p-btn"><svg width="13" height="12" viewBox="0 0 13 12"><path d="M6.5 11L1.5 6A3 3 0 016.5 2a3 3 0 015 4z" fill="#d787a8"/></svg></span><span class="p-btn"><svg width="14" height="12" viewBox="0 0 14 12"><path d="M1 1h2l2 7h7l1-5H4" stroke="#d787a8" stroke-width="1.5" fill="none"/><circle cx="6" cy="10.5" r="1" fill="#d787a8"/><circle cx="11" cy="10.5" r="1" fill="#d787a8"/></svg></span><span class="p-price">€0.00</span></div></div>
<div class="abs product" style="left:390px;top:549px"><div class="product-photo" role="img" aria-label="Photo of a handmade New Year card"></div><div class="product-meta">Lina Corvath<span class="sep">|</span>Runa<br>Naujieji metai</div><div class="product-actions"><span class="p-btn"><svg width="13" height="12" viewBox="0 0 13 12"><path d="M6.5 11L1.5 6A3 3 0 016.5 2a3 3 0 015 4z" fill="#d787a8"/></svg></span><span class="p-btn"><svg width="14" height="12" viewBox="0 0 14 12"><path d="M1 1h2l2 7h7l1-5H4" stroke="#d787a8" stroke-width="1.5" fill="none"/><circle cx="6" cy="10.5" r="1" fill="#d787a8"/><circle cx="11" cy="10.5" r="1" fill="#d787a8"/></svg></span><span class="p-price">€0.00</span></div></div>
<div class="abs product" style="left:542px;top:549px"><div class="product-photo" role="img" aria-label="Photo of a handmade New Year card"></div><div class="product-meta">Lina Corvath<span class="sep">|</span>Runa<br>Naujieji metai</div><div class="product-actions"><span class="p-btn"><svg width="13" height="12" viewBox="0 0 13 12"><path d="M6.5 11L1.5 6A3 3 0 016.5 2a3 3 0 015 4z" fill="#d787a8"/></svg></span><span class="p-btn"><svg width="14" height="12" viewBox="0 0 14 12"><path d="M1 1h2l2 7h7l1-5H4" stroke="#d787a8" stroke-width="1.5" fill="none"/><circle cx="6" cy="10.5" r="1" fill="#d787a8"/><circle cx="11" cy="10.5" r="1" fill="#d787a8"/></svg></span><span class="p-price">€0.00</span></div></div>

<div class="abs product" style="left:237px;top:786px"><div class="product-photo" role="img" aria-label="Photo of a handmade New Year card"></div><div class="product-meta">Lina Corvath<span class="sep">|</span>Runa<br>Naujieji metai</div><div class="product-actions"><span class="p-btn"><svg width="13" height="12" viewBox="0 0 13 12"><path d="M6.5 11L1.5 6A3 3 0 016.5 2a3 3 0 015 4z" fill="#d787a8"/></svg></span><span class="p-btn"><svg width="14" height="12" viewBox="0 0 14 12"><path d="M1 1h2l2 7h7l1-5H4" stroke="#d787a8" stroke-width="1.5" fill="none"/><circle cx="6" cy="10.5" r="1" fill="#d787a8"/><circle cx="11" cy="10.5" r="1" fill="#d787a8"/></svg></span><span class="p-price">€0.00</span></div></div>
<div class="abs product" style="left:390px;top:786px"><div class="product-photo" role="img" aria-label="Photo of a handmade New Year card"></div><div class="product-meta">Lina Corvath<span class="sep">|</span>Runa<br>Naujieji metai</div><div class="product-actions"><span class="p-btn"><svg width="13" height="12" viewBox="0 0 13 12"><path d="M6.5 11L1.5 6A3 3 0 016.5 2a3 3 0 015 4z" fill="#d787a8"/></svg></span><span class="p-btn"><svg width="14" height="12" viewBox="0 0 14 12"><path d="M1 1h2l2 7h7l1-5H4" stroke="#d787a8" stroke-width="1.5" fill="none"/><circle cx="6" cy="10.5" r="1" fill="#d787a8"/><circle cx="11" cy="10.5" r="1" fill="#d787a8"/></svg></span><span class="p-price">€0.00</span></div></div>
<div class="abs product" style="left:542px;top:786px"><div class="product-photo" role="img" aria-label="Photo of a handmade New Year card"></div><div class="product-meta">Lina Corvath<span class="sep">|</span>Runa<br>Naujieji metai</div><div class="product-actions"><span class="p-btn"><svg width="13" height="12" viewBox="0 0 13 12"><path d="M6.5 11L1.5 6A3 3 0 016.5 2a3 3 0 015 4z" fill="#d787a8"/></svg></span><span class="p-btn"><svg width="14" height="12" viewBox="0 0 14 12"><path d="M1 1h2l2 7h7l1-5H4" stroke="#d787a8" stroke-width="1.5" fill="none"/><circle cx="6" cy="10.5" r="1" fill="#d787a8"/><circle cx="11" cy="10.5" r="1" fill="#d787a8"/></svg></span><span class="p-price">€0.00</span></div></div>

<div class="abs pager">
  <span class="pg" style="width:28px;text-align:right"><svg width="7" height="10" viewBox="0 0 7 10"><path d="M6 1L2 5l4 4" stroke="#fff" stroke-width="2" fill="none"/></svg></span>
  <span class="pg-cur">1</span><span class="pg">2</span><span class="pg">3</span><span class="pg">4</span><span class="pg">5</span>
  <svg width="7" height="10" viewBox="0 0 7 10"><path d="M1 1l4 4-4 4" stroke="#a08670" stroke-width="2" fill="none"/></svg>
  <span style="margin-left:8px;font-size:7px">Go to</span>
  <span class="pg-goto">15</span>
</div>
<div class="abs pager-links"><span>PREVIOUS PAGE</span><span>NEXT PAGE</span></div>

<div class="abs social fw" style="top:723px">Friendwall</div>
<div class="abs follow fw" style="top:780px">37k Followers</div>
<div class="abs social cl" style="top:809px">Chirpline</div>
<div class="abs follow cl" style="top:866px">36k Followers</div>
<div class="abs social cn" style="top:895px">Circlenet</div>
<div class="abs follow cn" style="top:952px">15k Followers</div>

<footer class="abs footer"></footer>
<div class="abs f-links">About us<br>How it works<br>Prices<br>Rules<br>Contacts</div>
<div class="abs f-copy">© 2014 velmorino</div>
<div class="abs news">
  <h3>JOIN THE NEWSLETTER</h3>
  <div class="news-field"><span class="news-icon"><svg width="11" height="8" viewBox="0 0 11 8"><rect x=".5" y=".5" width="10" height="7" fill="none" stroke="#984c40"/><path d="M.5.5l5 4 5-4" fill="none" stroke="#984c40"/></svg></span><span>yourname@postmelo.com</span></div>
  <div class="news-btn">SUBSCRIBE</div>
</div>

</body>
</html>
```